New (old) Business Card Design Project

I would like to purchase a customized version of a design you have previously submitted - https://www.artmarketly.example/design/7305126

I like the card above, and would like to use the same design, jus with my business name, HARLOWAY ASSET ADVISORS. I like the colors in the card above, as well as the font. The other side will have my name, company name, address, phone, email, website, plus disclosure text I will provide.

Target Market(s)

wealthy families

Industry/Entity Type

Financial Services

Contact Information for Business Card

logo on one side, on other my name, company, address, phone, email, website, disclosure language I will provide.

Colors

Designer to choose colors to be used in the design.

Requirements
Must have
• colors: Deep blue and white
Nice to have
• Please see the items I have uploaded, below.
Should not have
• Cheap, tacky look.

```html
<!DOCTYPE html>
<html lang="en">
<head>
<meta charset="utf-8">
<title>Harloway Asset Advisors – Business Card</title>
<link rel="stylesheet" href="https://fonts.googleapis.com/css2?family=Open+Sans:wght@400;600;700&display=swap">
<style>
  :root {
    --stage: #e9eaec;
    --card-white: #ffffff;
    --navy: #1b3461;
    --navy-deep: #15294d;
    --ink: #1e1e1e;
    --pale: #dfe3ea;
    --pale-soft: #c3cad5;
    --rule: #2a2a2a;
  }
  * { margin: 0; padding: 0; box-sizing: border-box; }
  html, body { width: 1200px; height: 900px; overflow: hidden; }
  body {
    background: var(--stage);
    position: relative;
    font-family: "Open Sans", Arial, sans-serif;
  }
  .card {
    position: absolute;
    left: 300px;
    width: 600px;
    height: 343px;
    box-shadow: 0 6px 18px rgba(0,0,0,0.18);
  }
  .card-front { top: 70px; background: var(--card-white); }
  .card-back {
    top: 487px;
    background: linear-gradient(160deg, var(--navy) 0%, var(--navy-deep) 100%);
  }

  /* Contact side */
  .identity {
    position: absolute;
    left: 0;
    width: 268px;
    top: 146px;
    text-align: right;
  }
  .identity .name {
    color: var(--navy);
    font-weight: 600;
    font-size: 18px;
    letter-spacing: 0.3px;
    line-height: 1.15;
  }
  .identity .role {
    color: var(--ink);
    font-weight: 700;
    font-size: 11.5px;
    letter-spacing: 0.3px;
    margin-top: 3px;
  }
  .divider {
    position: absolute;
    left: 286px;
    top: 140px;
    width: 2px;
    height: 92px;
    background: var(--rule);
  }
  .contact {
    position: absolute;
    left: 302px;
    top: 162px;
    list-style: none;
    color: var(--ink);
    font-size: 12.5px;
    font-weight: 600;
    line-height: 17px;
    letter-spacing: 0.2px;
  }
  .contact .web { color: var(--navy); font-weight: 700; }

  /* Brand side */
  .brand {
    position: absolute;
    left: 0; right: 0;
    top: 128px;
    text-align: center;
    font-family: "Open Sans", Arial, sans-serif;
    font-weight: 400;
    font-size: 28px;
    letter-spacing: 3px;
    color: var(--pale);
  }
  .tagline {
    position: absolute;
    left: 0; right: 0;
    top: 262px;
    text-align: center;
    font-family: "Open Sans", Arial, sans-serif;
    font-weight: 400;
    font-size: 11px;
    letter-spacing: 7px;
    color: var(--pale-soft);
  }
</style>
</head>
<body>
  <section class="card card-front" aria-label="Business card, contact side">
    <div class="identity">
      <p class="name">DANIEL WHITCOMBE</p>
      <p class="role">MANAGING DIRECTOR</p>
    </div>
    <div class="divider"></div>
    <ul class="contact">
      <li>TEL: XXX XXX XXXX</li>
      <li>FAX: XXX XXX XXXX</li>
      <li>EMAIL: daniel@harlowayaa.com</li>
      <li class="web">www.harlowayaa.com</li>
    </ul>
  </section>

  <section class="card card-back" aria-label="Business card, brand side">
    <p class="brand">HARLOWAY ASSET ADVISORS</p>
    <p class="tagline">PLAN • PRESERVE • PROSPER</p>
  </section>
</body>
</html>
```